Yard sign design for high end luxury home builder.

Need a design for signage on custom homes that are being built. I already have a logo that I am satisfied with that needs to be incorporated. I need the following incorporated in the design of the sign-
- Lic number 318562
- phone number (555) 271-4038
- pendrickhomeworks.com
- Logo/Branding

If possible it may be nice to have the following quote that is on are business cards-

Quote from Osmund of Veltarra-
HE WHO WORKS WITH HIS HANDS IS A LABORER.
HE WHO WORKS WITH HIS HANDS & HIS HEAD IS A CRAFTSMAN.
HE WHO WORKS WITH HIS HANDS & HIS HEAD & HIS HEART IS AN ARTISAN.
-OSMUND OF VELTARRA

Target Market(s)

Archetect, Designers, Clients desiring to build a new home or remodel.

Colors
fde9d4
fee4d5
fabb94
fac994
faa54b
f68d4d
f37122
f78f20
f68e4e

Requirements
Must have
• - Lic number 318562
• - phone number (555) 271-4038
• - pendrickhomeworks.com
• - Logo/Branding
Nice to have
• Quote from Osmund of Veltarra-
• HE WHO WORKS WITH HIS HANDS IS A LABORER.
• HE WHO WORKS WITH HIS HANDS & HIS HEAD IS A CRAFTSMAN.
• HE WHO WORKS WITH HIS HANDS & HIS HEAD & HIS HEART IS AN ARTISAN.
• -OSMUND OF VELTARRA
• OR the below statement-
• Craftsmen that Care
Should not have
• Any additional verbiage not specified above including any type of verbiage about what kind of company we are. For instance- Integrity, reputable... It's just all played out. Im just looking for a bitching design that has the info that compliments my logo/branding.

```html
<!DOCTYPE html>
<html lang="en">
<head>
<meta charset="utf-8">
<title>Pendrick Homeworks Yard Sign</title>
<link href="https://fonts.googleapis.com/css2?family=Anton&family=Open+Sans:wght@600;700;800&display=swap" rel="stylesheet">
<style>
  :root {
    --charcoal: #2b2a29;
    --orange: #f37122;
    --orange-light: #f68d4d;
    --orange-warm: #f78f20;
    --tan: #a88e72;
    --white: #ffffff;
    --backdrop: #f1f0ee;
  }
  html, body {
    margin: 0;
    padding: 0;
    width: 1200px;
    height: 1000px;
    overflow: hidden;
    background: var(--backdrop);
  }
  .canvas {
    position: relative;
    width: 1200px;
    height: 1000px;
  }
  .yard-sign {
    position: absolute;
    left: 245px;
    top: 30px;
    width: 710px;
    height: 940px;
    box-shadow: 0 6px 24px rgba(0,0,0,0.18);
  }
  .yard-sign svg { display: block; }
  .brand-name {
    font-family: "Open Sans", sans-serif;
    font-weight: 800;
    fill: var(--tan);
  }
  .quote-line {
    font-family: "Anton", sans-serif;
  }
  .license-label, .license-number {
    font-family: "Open Sans", sans-serif;
    font-weight: 700;
  }
  .contact-phone, .contact-web {
    font-family: "Open Sans", sans-serif;
    font-weight: 700;
    fill: var(--white);
  }
</style>
</head>
<body>
<div class="canvas">
  <div class="yard-sign">
    <svg width="710" height="940" viewBox="0 0 710 940" xmlns="http://www.w3.org/2000/svg">
      <defs>
        <radialGradient id="concreteFill" cx="50%" cy="50%" r="70%">
          <stop offset="0%" stop-color="#f2f1ef"/>
          <stop offset="100%" stop-color="#dcdbd8"/>
        </radialGradient>
        <linearGradient id="quoteFill" x1="0" y1="0" x2="0" y2="1">
          <stop offset="0%" stop-color="#f68d4d"/>
          <stop offset="100%" stop-color="#f37122"/>
        </linearGradient>
        <linearGradient id="lowerSwoosh" x1="0" y1="0" x2="1" y2="0">
          <stop offset="0%" stop-color="#f37122" stop-opacity="0.2"/>
          <stop offset="40%" stop-color="#f37122"/>
          <stop offset="100%" stop-color="#f37122"/>
        </linearGradient>
      </defs>

      <rect class="sign-body" width="710" height="940" fill="url(#concreteFill)"/>

      <!-- header band -->
      <path class="header-swoosh" d="M0 200 Q355 540 710 218 Q355 470 0 200 Z" fill="var(--orange)"/>
      <path class="header-band" d="M0 0 H710 V218 Q355 440 0 205 Z" fill="var(--charcoal)"/>

      <!-- footer band -->
      <path class="footer-swoosh" d="M0 836 Q355 580 710 764 V819 Q355 614 0 846 Z" fill="url(#lowerSwoosh)"/>
      <path class="footer-band" d="M0 940 V846 Q355 614 710 819 V940 Z" fill="var(--charcoal)"/>

      <!-- brand -->
      <g class="brand">
        <rect x="305" y="50" width="100" height="100" fill="var(--tan)"/>
        <text class="brand-name" x="355" y="222" font-size="40" text-anchor="middle" letter-spacing="3">PENDRICK</text>
        <text class="brand-name" x="355" y="250" font-size="15" text-anchor="middle" letter-spacing="2">HOMEWORKS INC.</text>
      </g>

      <!-- quote -->
      <g class="quote" fill="url(#quoteFill)">
        <text class="quote-line" x="82" y="455" font-size="64" textLength="555" lengthAdjust="spacingAndGlyphs">HE WHO WORKS WITH</text>
        <text class="quote-line" x="82" y="573" font-size="124" textLength="555" lengthAdjust="spacingAndGlyphs">HIS HANDS</text>
        <text class="quote-line" x="82" y="669" font-size="102" textLength="555" lengthAdjust="spacingAndGlyphs" fill="var(--orange-warm)">IS A LABORER</text>
      </g>

      <!-- license -->
      <g class="license">
        <rect x="208" y="780" width="323" height="48" fill="none" stroke="var(--white)" stroke-width="1.5"/>
        <text x="370" y="814" text-anchor="middle" font-size="27">
          <tspan class="license-label" fill="var(--orange-warm)">LIC NUMBER </tspan><tspan class="license-number" fill="var(--white)">318562</tspan>
        </text>
      </g>

      <!-- contact -->
      <g class="contact">
        <g class="icon-phone" transform="translate(48 858)" fill="none" stroke="var(--orange-warm)" stroke-width="4" stroke-linecap="round">
          <path d="M6 4 L12 2 L16 11 L12 14 Q15 22 22 26 L25 22 L33 27 L31 33 Q18 34 8 22 Q2 12 6 4 Z" fill="var(--orange-warm)" stroke="none"/>
          <path d="M22 6 Q30 8 31 16"/>
          <path d="M22 0 Q36 2 37 16"/>
        </g>
        <text class="contact-phone" x="96" y="889" font-size="36">(555) 271-4038</text>
        <rect x="384" y="858" width="2" height="42" fill="var(--white)"/>
        <g class="icon-globe" transform="translate(409 879)" fill="none" stroke="var(--orange-warm)" stroke-width="1.8">
          <circle r="10"/>
          <ellipse rx="4.5" ry="10"/>
          <line x1="-10" y1="0" x2="10" y2="0"/>
          <line x1="-8.5" y1="-5" x2="8.5" y2="-5"/>
          <line x1="-8.5" y1="5" x2="8.5" y2="5"/>
        </g>
        <text class="contact-web" x="426" y="886" font-size="21">pendrickhomeworks.com</text>
      </g>
    </svg>
  </div>
</div>
</body>
</html>
```